Business card design needed

Hi.
We need a business card for a building and construction business which specialises in all aspects of domestic building. This includes new and existing works, insurance and shop front works.
We would like to see designs similar to the pic attached.the idea that we are having is a universal card that can be used on shirts,the side of a ute and trailer,fridge magnets this like this, this card will need to be easy to read from advertising point of veiw ie ( ute in transit) a mixer of Blue's would be the main colours for any logo's or graphics and light colours or even white as the back ground choice as we want to stand out against white car. and easy to read while traveling please find some samples of what we like

Target Market(s)

other builders, home owners, insurance builders, anyone who may need work done to their properties home or business

Industry/Entity Type

Construction

Contact Information for Business Card

Company name: Colin Dartmoor Constructions
Name: Colin Dartmoor
Mobile: 0461735920
Address: POBox 728 Werribee
Email: colindartmoor@maildrop-example.com.au

Requirements
Must have
• Must have:
Name: Colin Dartmoor
Mobile: 0461735920
ABN: 47 803 516 229
The background needs to be able to be put onto car doors and onto tshirts.
Nice to have
• could have a slogan like "the person to bring ur dreams to reality" "done right the first time" "for allMatainace and construction needs" doesnt have to be one of those but something like that
Should not have
• nothing like clip art or basic font

```html
<!DOCTYPE html>
<html lang="en">
<head>
<meta charset="utf-8">
<title>Colin Dartmoor Constructions — Business Card</title>
<link href="https://fonts.googleapis.com/css2?family=Noto+Serif:wght@400;700&display=swap" rel="stylesheet">
<style>
  :root {
    --page-bg: #e9ecef;
    --card-white: #f6f7f8;
    --brand-blue: #1f9fd6;
    --brand-deep: #0a5f85;
    --ink-grey: #6b6f73;
    --ghost-grey: #e3e5e7;
    --back-glow: #2bb3e8;
    --back-mid: #0b7fb0;
    --back-edge: #043a55;
    --white: #ffffff;
  }
  * { margin: 0; padding: 0; box-sizing: border-box; }
  html, body { width: 1200px; height: 900px; overflow: hidden; }
  body {
    background: var(--page-bg);
    font-family: "Noto Serif", Georgia, serif;
    position: relative;
  }
  .card {
    position: absolute;
    left: 280px;
    width: 640px;
    height: 390px;
    overflow: hidden;
    box-shadow: 0 6px 18px rgba(0,0,0,0.18);
  }
  /* Front */
  .card--front { top: 30px; background: var(--card-white); }
  .front__ghost {
    position: absolute;
    right: -90px;
    top: 40px;
    width: 380px;
    height: 380px;
    border-radius: 50%;
    background: var(--ghost-grey);
  }
  .brand {
    position: absolute;
    left: 40px;
    top: 36px;
    display: flex;
    align-items: center;
    gap: 18px;
  }
  .brand__dot {
    width: 74px;
    height: 74px;
    border-radius: 50%;
    background: var(--brand-blue);
    flex: none;
  }
  .brand__name {
    font-weight: 700;
    font-size: 34px;
    line-height: 1.05;
    color: var(--brand-deep);
    width: 340px;
  }
  .contact {
    position: absolute;
    left: 56px;
    top: 190px;
  }
  .contact__name {
    font-size: 30px;
    color: var(--brand-blue);
    margin-bottom: 14px;
  }
  .contact__line {
    font-size: 16px;
    color: var(--ink-grey);
    line-height: 1.45;
  }
  .label { color: var(--brand-blue); }
  .abn {
    position: absolute;
    right: 40px;
    bottom: 34px;
    font-size: 17px;
    color: var(--ink-grey);
  }
  /* Back */
  .card--back {
    top: 480px;
    background: radial-gradient(ellipse at 52% 38%, var(--back-glow) 0%, var(--back-mid) 40%, var(--back-edge) 100%);
    display: flex;
    flex-direction: column;
    align-items: center;
    text-align: center;
    padding-top: 44px;
  }
  .back__dot {
    width: 110px;
    height: 110px;
    border-radius: 50%;
    background: var(--white);
    margin-bottom: 20px;
  }
  .back__name {
    font-weight: 700;
    font-size: 40px;
    line-height: 1.05;
    color: var(--white);
    margin-bottom: 22px;
  }
  .services {
    font-size: 16px;
    color: var(--white);
    line-height: 1.5;
    letter-spacing: 0.3px;
  }
</style>
</head>
<body>
  <section class="card card--front" aria-label="Business card front">
    <div class="front__ghost" aria-hidden="true"></div>
    <div class="brand">
      <div class="brand__dot" aria-hidden="true"></div>
      <div class="brand__name">Colin Dartmoor Constructions</div>
    </div>
    <div class="contact">
      <p class="contact__name">Colin Dartmoor</p>
      <p class="contact__line"><span class="label">M:</span> 0461735920</p>
      <p class="contact__line"><span class="label">E:</span> colindartmoor@maildrop-example.com.au</p>
    </div>
    <p class="abn"><span class="label">ABN:</span> 47 803 516 229</p>
  </section>

  <section class="card card--back" aria-label="Business card back">
    <div class="back__dot" aria-hidden="true"></div>
    <div class="back__name">Colin Dartmoor<br>Constructions</div>
    <p class="services">Renovation / Insurance Work / Project Management<br>All Forms Of Carpentry</p>
  </section>
</body>
</html>
```